Billboard design - consider what a billboard is

Design a billboard using my logo - Billboard is 6m x 3m
A Billboard is advertising for my company that is on a big sign.

Has to be clean and easy to read, and ideally highlights that we are Residential and Commercial builders.

Keep it clean and easy to read

The contact number for the board is

022 583 7092
www.harbourframeworks.co.nz
info@harbourframeworks.co.nz

Doesnt have to have all contact details if it doesnt fit

Has to catch peoples attention to contact us if they need a builder

Can you please change the sign to be all white writing, with black background ?
Updates

Please consider what a billboard is...

The design needs to be suitable for a billboard..

Target Market(s)

people driving past

Industry/Entity Type

Construction

Logo Text

Wellington Builder, website email address, contact number

Colors
0054AA
0677BA
7BADD7
CADEEF
E8F1F8

Requirements
Must have
• Easy to read
Nice to have
• easy to read, can clearly see contact details

```html
<!DOCTYPE html>
<html lang="en">
<head>
<meta charset="utf-8">
<title>Harbour Frameworks – Wellington Builder Billboard</title>
<link href="https://fonts.googleapis.com/css2?family=Roboto+Condensed:wght@400;700;900&display=swap" rel="stylesheet">
<style>
  :root {
    --navy-deep: #15224a;
    --navy-mid: #22336a;
    --navy-light: #34477e;
    --brand-blue: #5f8fcb;
    --band-blue: #6391c9;
    --headline-yellow: #dfe443;
    --white: #ffffff;
    --icon-ring: #f1f1f1;
    --orange-light: #f9b778;
    --orange-dark: #e2682a;
    --photo-light: rgba(225, 230, 240, 0.22);
    --photo-vest: rgba(205, 222, 70, 0.42);
  }
  * { margin: 0; padding: 0; box-sizing: border-box; }
  html, body { width: 1200px; height: 600px; overflow: hidden; background: var(--navy-deep); }
  .billboard {
    position: relative;
    width: 1200px;
    height: 600px;
    overflow: hidden;
    font-family: "Roboto Condensed", "Arial Narrow", sans-serif;
    color: var(--white);
  }
  .backdrop-photo {
    position: absolute; inset: 0;
    background:
      radial-gradient(ellipse at 45% 40%, var(--navy-light) 0%, transparent 60%),
      linear-gradient(180deg, var(--navy-mid) 0%, var(--navy-deep) 100%);
  }
  .worker-photo {
    position: absolute;
    left: 800px; top: 24px;
    width: 400px; height: 576px;
    background: linear-gradient(180deg, var(--photo-light) 0%, var(--photo-light) 35%, var(--photo-vest) 100%);
  }
  .brand {
    position: absolute;
    left: 52px; top: 88px;
    display: flex; align-items: center; gap: 14px;
  }
  .brand-mark {
    width: 20px; height: 20px;
    background: var(--brand-blue);
  }
  .brand-name {
    font-weight: 700;
    font-size: 46px;
    line-height: 1;
    color: var(--brand-blue);
  }
  .headline {
    position: absolute;
    left: 42px; top: 180px;
    font-weight: 900;
    font-size: 122px;
    line-height: 1;
    color: var(--headline-yellow);
    letter-spacing: -0.5px;
    white-space: nowrap;
  }
  .service-band {
    position: absolute;
    left: 0; top: 323px;
    width: 913px; height: 79px;
    background: var(--band-blue);
    display: flex; align-items: center;
    padding-left: 42px;
  }
  .service-text {
    font-weight: 400;
    font-size: 53px;
    line-height: 1;
    color: var(--white);
    white-space: nowrap;
  }
  .contact-row {
    position: absolute;
    display: flex; align-items: center;
  }
  .contact-row.phone { left: 56px; top: 406px; height: 100px; }
  .contact-row.web { left: 53px; top: 511px; height: 72px; }
  .contact-icon { flex: none; }
  .phone .contact-icon { width: 68px; height: 68px; }
  .web .contact-icon { width: 72px; height: 72px; }
  .phone-number {
    margin-left: 34px;
    font-weight: 700;
    font-size: 100px;
    line-height: 1;
    white-space: nowrap;
  }
  .web-address {
    margin-left: 32px;
    font-weight: 700;
    font-size: 47px;
    line-height: 1;
    white-space: nowrap;
  }
</style>
</head>
<body>
  <div class="billboard">
    <div class="backdrop-photo" role="img" aria-label="Modern multi-storey apartment buildings at dusk, tinted deep navy"></div>
    <div class="worker-photo" role="img" aria-label="Photo of a smiling builder in a hard hat and hi-vis vest holding rolled building plans"></div>

    <div class="brand">
      <span class="brand-mark"></span>
      <span class="brand-name">Harbour Frameworks</span>
    </div>

    <h1 class="headline">Wellington Builder</h1>

    <div class="service-band">
      <p class="service-text">Residential &amp; Commercial Construction</p>
    </div>

    <div class="contact-row phone">
      <svg class="contact-icon" viewBox="0 0 68 68" aria-hidden="true">
        <defs>
          <radialGradient id="orangeGlowPhone" cx="50%" cy="35%" r="65%">
            <stop offset="0%" stop-color="#f9b778"/>
            <stop offset="100%" stop-color="#e2682a"/>
          </radialGradient>
        </defs>
        <circle cx="34" cy="34" r="33" fill="#f1f1f1"/>
        <circle cx="34" cy="34" r="28" fill="url(#orangeGlowPhone)"/>
        <path d="M20 30 q0-7 14-7 q14 0 14 7 l0 3 l-7 0 l0-4 q-7-2-14 0 l0 4 l-7 0 z" fill="#fff"/>
        <path d="M24 34 h20 l3 12 h-26 z" fill="#fff"/>
        <circle cx="34" cy="40" r="3.5" fill="#e2682a"/>
      </svg>
      <span class="phone-number">022 583 7092</span>
    </div>

    <div class="contact-row web">
      <svg class="contact-icon" viewBox="0 0 68 68" aria-hidden="true">
        <defs>
          <radialGradient id="orangeGlowWeb" cx="50%" cy="35%" r="65%">
            <stop offset="0%" stop-color="#f9b778"/>
            <stop offset="100%" stop-color="#e2682a"/>
          </radialGradient>
        </defs>
        <circle cx="34" cy="34" r="33" fill="#f1f1f1"/>
        <circle cx="34" cy="34" r="28" fill="url(#orangeGlowWeb)"/>
        <g fill="none" stroke="#fff" stroke-width="2.2">
          <circle cx="34" cy="34" r="14"/>
          <ellipse cx="34" cy="34" rx="6" ry="14"/>
          <line x1="20" y1="34" x2="48" y2="34"/>
          <path d="M22 26 h24 M22 42 h24"/>
        </g>
      </svg>
      <span class="web-address">www.harbourframeworks.co.nz</span>
    </div>
  </div>
</body>
</html>
```